limo company looking for a graphic business card with professional look and feel

Looking for a business card design that can give you the full picture of the limo company by looking at the card - we provide airport service, wedding, birthday, night out, etc... we have sedans, suvs , limos, and party buses. I want the business card to have a professional look because we are targetting corporate clients as well as regular retail.
Info about the business can be found at: http://qivroe.example/Tm3Kx7
Target Market(s)
corporate clients and retail
Industry/Entity Type
Business
Contact Information for Business Card
I would like the logo and the name of the company to be in raised print - not sure if design makes a difference for that or just print - I need it designed in 350dpi
Requirements
Must have
- pictures of vehicle types (sedans, suvs, limos, party bus). pictures of interior of the limos if possible. list service types (weddings, birthdays, proms, airport transportation) & service areas (houston, the woodlands, spring, tomball, cypress, kingwood).
Nice to have
- nice professional look to it.

```html
<!DOCTYPE html>
<html lang="en">
<head>
<meta charset="utf-8">
<title>Velmora Limousine – Business Card</title>
<link href="https://fonts.googleapis.com/css2?family=Cinzel:wght@400&family=Italianno&display=swap" rel="stylesheet">
<style>
  :root {
    --page: #e4e4e4;
    --card-front: #3a3a3a;
    --card-back: #1d1d1d;
    --card-edge: #2a2a2a;
    --line: #f2f2f2;
    --ink-dark: #2b2b2b;
    --type-light: #f4f4f4;
  }
  * { box-sizing: border-box; margin: 0; padding: 0; }
  html, body { width: 1043px; height: 1200px; overflow: hidden; }
  body { background: var(--page); position: relative; font-family: "Cinzel", serif; }

  .card { position: absolute; left: 60px; width: 913px; border: 4px solid var(--card-edge); }
  .card--front { top: 40px; height: 533px; background: var(--card-front); }
  .card--back { top: 612px; height: 528px; background: var(--card-back); }

  .frame { position: absolute; border: 3px solid var(--line); }
  .card--front .frame { left: 13px; top: 15px; width: 544px; height: 502px; }
  .card--back .frame { left: 15px; top: 15px; width: 882px; height: 497px; }

  .brand { position: absolute; left: 51px; top: 44px; color: var(--type-light); font-family: "Cinzel", serif; font-weight: 400; line-height: 1.1; }
  .brand__name { display: block; font-size: 27px; letter-spacing: 1px; }
  .brand__sub { display: block; font-size: 14px; letter-spacing: 1px; padding-left: 40px; }

  .pillar { position: absolute; width: 20px; bottom: 13px; background: var(--line); }
  .pillar--1 { left: 323px; top: 203px; }
  .pillar--2 { left: 362px; top: 236px; }
  .pillar--3 { left: 407px; top: 203px; }

  .gallery { position: absolute; left: 558px; top: 9px; width: 348px; height: 514px; background: var(--line); }
  .gallery__tile { position: absolute; }
  .tile--door     { left: 6px;   top: 6px;   width: 157px; height: 155px; background: linear-gradient(135deg, #cfcfcf, #4a4a4a 60%, #1a1a1a); }
  .tile--suit     { left: 172px; top: 6px;   width: 170px; height: 155px; background: linear-gradient(160deg, #2a2a2a, #0d0d0d); }
  .tile--toast    { left: 6px;   top: 168px; width: 157px; height: 150px; background: radial-gradient(circle at 50% 45%, #c9b98a, #5a4a35 55%, #1b1612); }
  .tile--lights   { left: 172px; top: 168px; width: 170px; height: 150px; background: radial-gradient(circle at 40% 50%, #b53a8a, #3a1440 50%, #0c0610); }
  .tile--interior { left: 6px;   top: 327px; width: 336px; height: 181px; background: linear-gradient(180deg, #1c2a5e, #2f4da0 55%, #121a3a); }

  .areas { position: absolute; left: 60px; top: 152px; width: 200px; list-style: none; text-align: center; color: var(--type-light); font-size: 17px; letter-spacing: 2px; line-height: 44px; }

  .fleet { position: absolute; background: var(--line); }
  .fleet__band { position: absolute; height: 22px; color: var(--ink-dark); font-size: 16px; letter-spacing: 2px; line-height: 22px; }
  .fleet--bus    { left: 320px; top: 97px;  width: 22px; bottom: 15px; }
  .fleet--bus .fleet__band    { left: 0; top: 0; width: 372px; background: var(--line); padding-left: 45px; }
  .fleet--suv    { left: 347px; top: 144px; width: 22px; bottom: 15px; }
  .fleet--suv .fleet__band    { left: 0; top: 0; width: 477px; background: var(--line); padding-left: 38px; word-spacing: 40px; }
  .fleet--sedan  { left: 389px; top: 188px; width: 20px; bottom: 15px; }
  .fleet--sedan .fleet__band  { left: 0; top: 0; width: 506px; background: var(--line); padding-left: 54px; }

  .city-night { position: absolute; left: 409px; top: 208px; width: 486px; height: 300px; background: radial-gradient(ellipse at 55% 60%, #6b5424, #2a2214 50%, #0b0a08); }
</style>
</head>
<body>
  <section class="card card--front">
    <div class="frame"></div>
    <div class="brand">
      <span class="brand__name">Velmora Limousine</span>
      <span class="brand__sub">&amp; Transportation</span>
    </div>
    <div class="pillar pillar--1"></div>
    <div class="pillar pillar--2"></div>
    <div class="pillar pillar--3"></div>
    <div class="gallery">
      <div class="gallery__tile tile--door" role="img" aria-label="Photo of a chauffeur opening a white limousine door"></div>
      <div class="gallery__tile tile--suit" role="img" aria-label="Photo of a black suit and tie"></div>
      <div class="gallery__tile tile--toast" role="img" aria-label="Photo of champagne glasses raised in a toast"></div>
      <div class="gallery__tile tile--lights" role="img" aria-label="Photo of colourful party lights"></div>
      <div class="gallery__tile tile--interior" role="img" aria-label="Photo of a party bus interior with blue lighting and leather seating"></div>
    </div>
  </section>

  <section class="card card--back">
    <div class="frame"></div>
    <ul class="areas">
      <li>Houston</li>
      <li>The Woodland</li>
      <li>Spring</li>
      <li>Tomball</li>
      <li>Cypress</li>
      <li>Kingwood</li>
    </ul>
    <div class="fleet fleet--bus"><div class="fleet__band">Party Bus</div></div>
    <div class="fleet fleet--suv"><div class="fleet__band">SUVS Limo</div></div>
    <div class="fleet fleet--sedan"><div class="fleet__band">Sedans</div></div>
    <div class="city-night" role="img" aria-label="Aerial photo of city streets lit at night"></div>
  </section>
</body>
</html>
```